Business Card for my New Brokerage

Looking to get a business card design for my new Real Estate Brokerage.
I want it with Picture, Phone Number, Email, Website, Office Address
Name and Designation. Please add logo too.

Target Market(s)

Real Estate Investors or Home Buyers

Industry/Entity Type

Real Estate

Contact Information for Business Card

Name, Email, Phone Number, website, email, office address

Colors
EB3D1F
EC4F4E
F09395
F8D3D4
FCEDEE

Requirements
Must have
• Minimalistic, Clean, Modern, Photo
Nice to have
• White and Red Colors

```html
<!DOCTYPE html>
<html lang="en">
<head>
<meta charset="utf-8">
<title>Ember Realty Inc – Business Card</title>
<link href="https://fonts.googleapis.com/css2?family=Montserrat:wght@400;500;700;800&display=swap" rel="stylesheet">
<style>
  :root {
    --red: #e0100f;
    --red-deep: #c80a0a;
    --red-light: #ec2a24;
    --gold: #d9b15c;
    --white: #ffffff;
    --ink: #3a3a3a;
    --bg: #1f1f1f;
    --bg-light: #2e2e2e;
  }
  * { margin: 0; padding: 0; box-sizing: border-box; }
  html, body { width: 1200px; height: 900px; overflow: hidden; }
  body {
    background: radial-gradient(circle at 70% 20%, var(--bg-light), var(--bg) 70%);
    font-family: "Montserrat", sans-serif;
    position: relative;
  }
  .card {
    position: absolute;
    left: 250px;
    width: 700px;
    height: 400px;
    border-radius: 26px;
    overflow: hidden;
  }
  .card-front {
    top: 40px;
    background: linear-gradient(135deg, var(--red-light), var(--red) 55%, var(--red-deep));
  }
  .card-back { top: 465px; background: var(--white); }

  .portrait {
    position: absolute;
    left: 0; top: 0;
    width: 300px; height: 400px;
    background: linear-gradient(180deg, #c89a83 0%, #b98a74 35%, #2a3144 60%, #1b2130 100%);
  }

  .brand {
    position: absolute;
    font-family: "Montserrat", sans-serif;
    text-align: center;
  }
  .brand-name {
    font-weight: 800;
    font-size: 72px;
    letter-spacing: 2px;
    line-height: 1;
  }
  .brand-sub {
    font-weight: 500;
    font-size: 20px;
    letter-spacing: 7px;
    margin-top: 4px;
  }
  .card-front .brand { left: 360px; top: 140px; width: 300px; color: var(--white); }
  .card-back .brand { right: 40px; top: 36px; width: 280px; color: var(--red); }
  .card-back .brand-name { font-size: 62px; }
  .card-back .brand-sub { font-size: 17px; letter-spacing: 6px; }

  .name-marker {
    position: absolute; left: 0; top: 138px;
    width: 12px; height: 46px; background: var(--red);
  }
  .person-name {
    position: absolute; left: 60px; top: 138px;
    color: var(--red); font-weight: 700; font-size: 34px; letter-spacing: 1px; line-height: 1.2;
  }
  .person-title {
    position: absolute; left: 60px; top: 182px;
    color: var(--ink); font-size: 19px; font-weight: 400;
  }
  .divider {
    position: absolute; left: 60px; top: 222px;
    width: 590px; height: 2px; background: var(--red);
  }
  .contact-list {
    position: absolute; left: 60px; top: 236px;
    list-style: none; color: var(--ink); font-size: 20px;
  }
  .contact-list li { display: flex; align-items: center; gap: 10px; height: 31px; }
  .contact-list svg { width: 16px; height: 16px; flex: none; }
  .address {
    position: absolute; right: 50px; top: 268px;
    text-align: right; color: var(--ink); font-size: 20px; line-height: 1.4; font-style: normal;
  }
  .bottom-band {
    position: absolute; left: 0; bottom: 0; width: 700px; height: 50px;
  }
</style>
</head>
<body>

<section class="card card-front">
  <div class="portrait" role="img" aria-label="Portrait photo of the broker in a dark blazer and light blue shirt"></div>
  <div class="brand">
    <div class="brand-name">EMBER</div>
    <div class="brand-sub">REALTY INC</div>
  </div>
</section>

<section class="card card-back">
  <div class="brand">
    <div class="brand-name">EMBER</div>
    <div class="brand-sub">REALTY INC</div>
  </div>

  <div class="name-marker"></div>
  <h1 class="person-name">DANIEL REYES</h1>
  <p class="person-title">Founder and President</p>
  <div class="divider"></div>

  <ul class="contact-list">
    <li>
      <svg viewBox="0 0 16 16"><path d="M4 1 L6 5 L4.5 6.5 Q6 10 9.5 11.5 L11 10 L15 12 L13.5 15 Q6 14 1 2.5 Z" fill="var(--red)"/></svg>
      +330 5120-4471
    </li>
    <li>
      <svg viewBox="0 0 16 16"><rect x="1.5" y="3.5" width="13" height="9" fill="none" stroke="var(--red)" stroke-width="1.5"/><path d="M1.5 3.5 L8 9 L14.5 3.5" fill="none" stroke="var(--red)" stroke-width="1.5"/></svg>
      info@emberrealtyinc.com
    </li>
    <li>
      <svg viewBox="0 0 16 16"><circle cx="8" cy="8" r="6.5" fill="none" stroke="var(--red)" stroke-width="1.5"/><ellipse cx="8" cy="8" rx="3" ry="6.5" fill="none" stroke="var(--red)" stroke-width="1.2"/><path d="M1.5 8 H14.5" stroke="var(--red)" stroke-width="1.2"/></svg>
      www.emberrealtyinc.com
    </li>
  </ul>

  <address class="address">
    1870 Cedar Hollow Lane<br>
    Maple Ridge, GA 30412
  </address>

  <svg class="bottom-band" viewBox="0 0 700 50" preserveAspectRatio="none">
    <path d="M0 12 L400 12 Q420 12 440 20 L0 20 Z" fill="var(--gold)"/>
    <path d="M0 20 L410 20 Q432 20 446 16 Q462 12 480 12 L700 12 L700 50 L0 50 Z" fill="var(--red)"/>
  </svg>
</section>

</body>
</html>
```